Southern Grain Assurance- Web & Business card design for a new business within the Ag Sector

HELLO!!!!

We need your help in relation to web design (business cards and stationary if possible!) for a new company based in NSW, Australia.

The name of the business is: Southern Grain Assurance (SGA). I have quickly mocked a webpage just to give you an idea of what we are looking for.... http://fieldmockup7.sitebuildly.example/http

SGA is a strategic advisory, investment manager and problem solver within the Australian Agricultural sector.

Our Mission:

We are here to provide solutions to ALL of our Clients needs and desires within the Agricultural space.

Our Team:

Our team has worked with some of the largest & oldest Agricultural companies in Australia

We provide our Clients with a unique blend of the best Corporate as well as Operational experience that the Industry has to offer.

Client-driven Services Approach:

SGA offers a tailored service in order to meet the objectives and outcomes for each and every client.

Some of our services include:

- Food Security / Supply

- Procurement strategies within and across agricultural supply-chains

- Strategic Agribusiness advice for both Australian and Chinese based agricultural enterprises

- M&A / Due Diligence

- Corporate governance & risk management strategies.

I have attached a copy of our capability statement for background reading.

We look forward to receiving your designs!!!!!!!
Updates

Target Market(s)

Corporate, Family Offices, Food Services & Supermarkets - that are looking to obtain products within the agricultural space. Whether it be boxed beef, grain, live animals, advice - ie M&A, Due diligence - just think anything "Agricultural" and we can provide a solution

Industry/Entity Type

Agriculture

Contact Information for Business Card

See below

With respect to the business cards:

There are 2 Managing Directors:

1. Martin Pellow
Managing Director
E: martin.pellow@southerngrainassurance.example
M: +61 491 203 664
W: www.southerngrainassurance.example

2. Kate Wrenley
Managing Director
E: kate.wrenley@southerngrainassurance.example
M: +61 432 796 018

Please see attached 2 * Files named Brenmoor that outline a layout of business card that I like

Coding

Coded - Design and coding required

Number of Pages Required

5+ page

Font styles to use
Sans Serif
Other font styles liked:
• Calibri

Requirements
Must have
• I like the look of this website: http://pastoralvx.example/
• And I like the themes in the website that I have mocked up: http://fieldmockup7.sitebuildly.example/http
• The wow factor, with a professional twist.
• With respect to the website - would like it to follow the flow of the capability statement - ie with a home page, and the four additional pages:
• ABOUT US
• OUR SERVICES
• OUR TEAM
• CONTACT DETAILS
• The powerpoint presentation that I have attached is simply there for content direction - not design direction.
• As a result, am looking for web design / business card that stands out - is corporate - yet still agricultural feel.
• "capability statement" simply refers to a document that outlines our capabilities - and does not form part of the business name.
• A black angus cow, or a stalk of wheat - greens and yellows may better represent the Ag space.
• This s a draft mock-up of a web-site I created with one of those free web-page makers... This should give you a feel - crisp - whites - yet agricultural tones to highlight
• The attachments below should be used as inspiration - and don't need to be the actual shots used.

```html
<!DOCTYPE html>
<html lang="en">
<head>
<meta charset="utf-8">
<title>Southern Grain Assurance</title>
<link href="https://fonts.googleapis.com/css2?family=Raleway:wght@400;500;600;700&display=swap" rel="stylesheet">
<style>
:root{
  --green:#8dd11f;
  --green-dark:#7bbd14;
  --ink:#3a3a3a;
  --muted:#777;
  --white:#fff;
  --topbar:rgba(40,40,40,.75);
  --panel:rgba(30,30,30,.72);
}
*{margin:0;padding:0;box-sizing:border-box}
html,body{width:1080px;height:1200px;overflow:hidden}
body{font-family:'Raleway',Arial,sans-serif;background:var(--white);color:var(--ink);position:relative}
.hero{position:absolute;left:0;top:0;width:1080px;height:508px;
  background:linear-gradient(180deg,#6f9fc9 0%,#a9c6de 35%,#dfe8ee 58%,#7da34a 72%,#4f7f2a 86%,#5d8f2c 100%)}
.topbar{position:absolute;left:0;top:0;width:1080px;height:31px;background:var(--topbar);
  color:#eee;font-size:12px;display:flex;align-items:center;padding-left:90px;gap:8px}
.topbar svg{width:11px;height:11px}
.header{position:absolute;left:78px;top:44px;width:928px;height:54px;background:rgba(255,255,255,.85);
  display:flex;align-items:center;padding-left:6px}
.brand{display:flex;align-items:center;gap:10px}
.brand-dot{width:46px;height:46px;border-radius:50%;background:var(--green)}
.brand-text{display:flex;flex-direction:column;line-height:1}
.brand-name{font-size:34px;font-weight:700;color:#7a7a7a;letter-spacing:1px}
.brand-tag{font-size:11px;font-weight:600;color:var(--green-dark)}
.nav{margin-left:auto;display:flex;gap:30px;padding-right:20px;font-size:12.5px;font-weight:600;color:#333}
.hero-mark{position:absolute;left:514px;top:197px;width:54px;height:54px;border-radius:50%;background:var(--green)}
.hero-title{position:absolute;left:0;width:1080px;top:266px;text-align:center;color:#fff;font-size:45px;font-weight:400;
  text-shadow:0 1px 3px rgba(0,0,0,.3)}
.hero-title b{font-weight:700}
.hero-sub{position:absolute;left:50%;transform:translateX(-50%);top:346px;height:36px;padding:0 9px;background:var(--green);color:#fff;
  font-size:18px;text-align:center;line-height:36px;white-space:nowrap}
.hero-sub::after{content:"";position:absolute;left:50%;margin-left:-7px;bottom:-7px;border:7px solid transparent;border-bottom:0;border-top-color:var(--green)}
.arrow{position:absolute;top:236px;width:31px;height:30px;background:rgba(60,60,60,.6);display:flex;align-items:center;justify-content:center}
.arrow.left{left:7px;border-radius:0 8px 8px 0}
.arrow.right{right:7px;border-radius:8px 0 0 8px}
.dots{position:absolute;top:484px;left:514px;display:flex;gap:10px}
.dots i{width:8px;height:8px;border-radius:50%;background:rgba(255,255,255,.8)}
.dots i:first-child{background:var(--green)}
.band{position:absolute;left:0;top:508px;width:1080px;height:150px;background:var(--green);color:#fff;text-align:center}
.band-mark{width:54px;height:54px;border-radius:50%;background:#fff;margin:42px auto 0}
.band p{font-size:15px;margin-top:20px}
.band b{font-weight:700}
.features{position:absolute;left:0;top:658px;width:1080px;height:214px;display:flex;justify-content:center;padding-top:45px}
.feature{width:310px;text-align:center;padding:0 20px}
.feature+.feature{border-left:1px solid #e3e3e3}
.feature h3{font-size:15px;font-weight:400;color:#555;margin-bottom:14px}
.feature h3 b{font-weight:700}
.feature p{font-size:12px;line-height:19px;color:var(--muted)}
.services{position:absolute;left:0;top:872px;width:1080px;height:328px;
  background:radial-gradient(ellipse at 75% 40%,#5c6e35 0%,#3a3a28 45%,#2a2620 100%)}
.tab{position:absolute;left:481px;top:82px;width:119px;height:29px;background:var(--green);color:#fff;
  font-size:12px;font-weight:600;text-align:center;line-height:29px;border-radius:12px 0 12px 0}
.tab::after{content:"";position:absolute;left:53px;bottom:-6px;border:6px solid transparent;border-bottom:0;border-top-color:var(--green)}
.col-title{position:absolute;top:185px;color:#fff;font-size:18px;font-weight:600;letter-spacing:.6px}
.box{position:absolute;background:var(--panel);border-left:2px solid var(--green);color:#fff;font-size:14px;line-height:20px;padding:7px 10px}
.box-short{white-space:nowrap}
</style>
</head>
<body>
<section class="hero" role="img" aria-label="Photo of green rolling farmland under a blue sky with clouds"></section>
<div class="topbar">
  <svg viewBox="0 0 10 16" fill="#eee"><rect x="1" y="0" width="8" height="16" rx="1.5"/><rect x="2.5" y="2" width="5" height="10" fill="#444"/></svg>
  <span>+61 432 796 018 | +61 417 350 942</span>
  <svg viewBox="0 0 16 12" fill="none" stroke="#eee" stroke-width="1.5" style="margin-left:6px"><rect x="1" y="1" width="14" height="10"/><path d="M1 1l7 6 7-6"/></svg>
  <span>southern.grain@mailbox.example</span>
</div>
<header class="header">
  <div class="brand">
    <span class="brand-dot"></span>
    <span class="brand-text"><span class="brand-name">SGA</span><span class="brand-tag">Southern Grain Assurance</span></span>
  </div>
  <nav class="nav"><span>About Us</span><span>Our Services</span><span>Our Team</span><span>Contact Us</span></nav>
</header>
<div class="arrow left"><svg width="10" height="12" viewBox="0 0 10 12"><path d="M7 1L2 6l5 5" stroke="#ccc" stroke-width="2" fill="none"/></svg></div>
<div class="arrow right"><svg width="10" height="12" viewBox="0 0 10 12"><path d="M3 1l5 5-5 5" stroke="#ccc" stroke-width="2" fill="none"/></svg></div>
<div class="hero-mark"></div>
<h1 class="hero-title"><b>Southern</b> Grain Assurance</h1>
<div class="hero-sub">Solutions to <b>all of our clients needs and desires</b> within the Agricultural space</div>
<div class="dots"><i></i><i></i><i></i></div>

<section class="band">
  <div class="band-mark"></div>
  <p>We are a <b>strategic advisory, investment manager and problem solver</b> within the Australian Agricultural sector.</p>
</section>

<section class="features">
  <div class="feature"><h3><b>Strategic</b> advisors</h3><p>SGA is a strategic advisory, investment manager and problem solver within the Australian Agricultural sector.</p></div>
  <div class="feature"><h3><b>Client</b> solutions</h3><p>We are here to provide solutions to ALL of our Clients needs and desires within the Agricultural space.</p></div>
  <div class="feature"><h3><b>Experienced</b> people</h3><p>Our team has worked with some of the largest &amp; oldest Agricultural companies in Australia</p></div>
</section>

<section class="services" role="img" aria-label="Blurred photo of young crop rows in dark soil">
  <div class="tab">Our Services</div>
  <h2 class="col-title" style="left:89px">Client-driven Services Approach:</h2>
  <div class="box" style="left:89px;top:230px;width:440px">SGA offers a tailored service in order to meet the objectives and outcomes for each and every client.</div>
  <h2 class="col-title" style="left:552px">Some of our services include:</h2>
  <div class="box box-short" style="left:552px;top:212px">Food Security / Supply</div>
  <div class="box" style="left:552px;top:256px;width:440px">Procurement strategies within and across agricultural supply-chains</div>
</section>
</body>
</html>
```